Amber Lantern Cafe Business Card

We need a business card design for a new European Cafe. Main menu will be coffee and deserts.

Requirements
Must have
• Logo - 1 of the attached versions
Address - TBA (you can use 487 Morrow Ave Unit 9 for now)
Phone - TBA (you can use 555-238-4176 for now)

```html
<!DOCTYPE html>
<html lang="en">
<head>
<meta charset="utf-8">
<title>Amber Lantern Cafe – Business Card</title>
<link rel="stylesheet" href="https://fonts.googleapis.com/css2?family=Open+Sans:wght@400;600;700&display=swap">
<style>
  :root {
    --backdrop: #1f1c1b;
    --card-white: #f7f6f4;
    --espresso: #2e2826;
    --amber: #b5612f;
    --ink: #2b2523;
    --cream-text: #efeae6;
  }
  * { margin: 0; padding: 0; box-sizing: border-box; }
  html, body {
    width: 1200px; height: 800px; overflow: hidden;
    background: var(--backdrop);
    font-family: "Open Sans", Arial, sans-serif;
  }
  .stage {
    width: 1200px; height: 800px;
    display: flex; align-items: center; justify-content: center;
  }
  .business-card {
    position: relative;
    width: 840px; height: 480px;
    background: var(--card-white);
    overflow: hidden;
    box-shadow: 0 18px 40px rgba(0,0,0,.45);
  }
  .card-waves { position: absolute; inset: 0; width: 100%; height: 100%; }
  .card-waves .wave-band { fill: var(--amber); }
  .card-waves .wave-base { fill: var(--espresso); }

  .brand {
    position: absolute; left: 62px; top: 78px;
    display: flex; align-items: center; gap: 22px;
  }
  .brand-square {
    width: 108px; height: 108px;
    background: var(--ink);
    border-radius: 6px;
  }
  .brand-name {
    font-weight: 600; font-size: 40px; line-height: 1.1;
    color: var(--ink); letter-spacing: .2px;
  }

  .contact-person {
    position: absolute; right: 58px; top: 292px;
    text-align: right;
  }
  .person-name {
    font-weight: 700; font-size: 21px; letter-spacing: .5px;
    color: var(--amber); text-transform: uppercase;
  }
  .person-role { font-size: 16px; color: var(--cream-text); }

  .contact-details {
    position: absolute; left: 62px; bottom: 44px;
    color: var(--cream-text); font-size: 17px;
  }
  .contact-address { margin-bottom: 14px; }
  .contact-row { display: flex; align-items: center; gap: 26px; }
  .contact-item { display: flex; align-items: center; gap: 8px; }
  .contact-icon {
    width: 22px; height: 22px; border-radius: 50%;
    border: 1.5px solid var(--amber);
    display: flex; align-items: center; justify-content: center;
  }
  .contact-icon svg { width: 12px; height: 12px; fill: var(--amber); }
</style>
</head>
<body>
<main class="stage">
  <article class="business-card">
    <svg class="card-waves" viewBox="0 0 840 480" preserveAspectRatio="none" aria-hidden="true">
      <path class="wave-band" d="M0,268 C260,300 520,228 840,142 L840,168 C520,254 260,322 0,296 Z"/>
      <path class="wave-base" d="M0,306 C260,332 520,264 840,178 L840,480 L0,480 Z"/>
    </svg>

    <div class="brand">
      <div class="brand-square"></div>
      <div class="brand-name">Amber Lantern<br>Cafe</div>
    </div>

    <div class="contact-person">
      <div class="person-name">Nora Whitfield</div>
      <div class="person-role">Manager</div>
    </div>

    <div class="contact-details">
      <p class="contact-address">487 Morrow Ave Unit 9, Brookvale, ON K2P4R8</p>
      <div class="contact-row">
        <span class="contact-item">
          <span class="contact-icon">
            <svg viewBox="0 0 24 24" aria-hidden="true"><path d="M6.6 10.8a15.1 15.1 0 0 0 6.6 6.6l2.2-2.2a1 1 0 0 1 1-.25 11.4 11.4 0 0 0 3.6.6 1 1 0 0 1 1 1V20a1 1 0 0 1-1 1A17 17 0 0 1 3 4a1 1 0 0 1 1-1h3.5a1 1 0 0 1 1 1c0 1.25.2 2.45.6 3.6a1 1 0 0 1-.25 1z"/></svg>
          </span>
          555-238-4176
        </span>
        <span class="contact-item">
          <span class="contact-icon">
            <svg viewBox="0 0 24 24" aria-hidden="true"><path d="M3 5h18v14H3z M4 6.5v.3l8 5.2 8-5.2v-.3z" fill-rule="evenodd"/></svg>
          </span>
          info@amberlantern.com
        </span>
      </div>
    </div>
  </article>
</main>
</body>
</html>
```